TQR Habitat Stewards 2019

We need a 2 page flyer to advertise our upcoming program. The program covers 5 months May-September 2019 and is focused on conservation.I have attached some options that i like. It needs to be striking.

Text in newly uploaded document 'HSFlyer2'

Target Market(s)

Conservation
Conscious travelers
30-45 year olds
Environmental
Adventure/Hiking
Citizen Science

Font styles to use
Sans Serif

Colors
0355a3
fbed22

Requirements
Must have
• A travel conservation focus
• Highlight the significance of the 'in the world' status of the project
Nice to have
• A yellow border, making it look similar to the cover of Wanderfield Quarterly

```html
<!DOCTYPE html>
<html lang="en">
<head>
<meta charset="utf-8">
<title>TQR Habitat Stewards 2019 – Flyer</title>
<link rel="stylesheet" href="https://fonts.googleapis.com/css2?family=Montserrat:wght@500;600;700&family=Open+Sans:wght@400;600&family=Oswald:wght@500;600;700&family=Kaushan+Script&display=swap">
<style>
:root{
  --blue:#0355a3;
  --navy:#173a78;
  --yellow:#fbed22;
  --gold:#f8d317;
  --ink:#2a2f3a;
  --white:#ffffff;
  --stage:#ababab;
  --sea-deep:#0b3f6e;
  --sea:#1f78a8;
  --sky:#c9e2ee;
}
*{box-sizing:border-box;margin:0;padding:0}
html,body{width:1200px;height:950px;overflow:hidden}
body{background:var(--stage);position:relative;font-family:"Open Sans",Arial,sans-serif;color:var(--ink)}

.page{position:absolute;top:70px;width:548px;height:774px;border:3px solid #111;background:var(--gold);overflow:hidden}
.page--front{left:40px}
.page--back{left:614px;background:linear-gradient(180deg,var(--gold) 0%,var(--gold) 58%,#fff 72%)}

/* ---------- front ---------- */
.front-inner{position:absolute;left:17px;top:19px;right:17px;bottom:0;background:var(--white);overflow:hidden}
.scenery{position:absolute;left:0;right:0;top:140px;bottom:0;
  background:linear-gradient(180deg,var(--sky) 0%,#8fc2d9 12%,var(--sea) 28%,var(--sea-deep) 56%,#1d3b2a 80%,#14231a 100%)}
.brand{position:absolute;left:14px;top:10px;width:68px;text-align:center;color:var(--blue);font-family:"Montserrat",sans-serif;font-weight:700;font-size:8px;line-height:1.15}
.brand__dot{display:block;width:34px;height:34px;border-radius:50%;border:3px solid var(--blue);margin:0 auto 3px}
.headline{position:absolute;left:108px;top:16px;width:240px;font-family:"Kaushan Script",cursive;font-weight:400;font-size:27px;line-height:40px;color:var(--blue);white-space:nowrap}
.headline__year{position:absolute;left:350px;top:8px;width:128px;height:52px;background:var(--yellow);font-family:"Oswald",sans-serif;font-weight:700;font-size:38px;line-height:52px;text-align:center;color:var(--blue)}
.intro{position:absolute;left:24px;right:24px;text-align:center;font-size:10.5px;line-height:13.5px;color:#333}
.intro--top{top:78px}
.intro--over{top:166px;color:#1d2a3a}
.quote{position:absolute;left:0;right:0;top:133px;text-align:center;font-family:"Montserrat",sans-serif;font-weight:600;font-size:10px;line-height:13px;color:#222}
.quote cite{display:block;font-style:normal;font-size:9px;margin-left:150px}

.event__box{position:absolute;background:rgba(255,255,255,.96);padding:6px 8px 6px 26px}
.event__title{font-family:"Montserrat",sans-serif;font-weight:700;font-size:10px;line-height:13px;color:var(--navy);text-transform:uppercase;margin-bottom:2px;white-space:nowrap}
.event__text{font-size:7.2px;line-height:9.6px;color:#333}
.event__photo{position:absolute;border-radius:50%;border:5px solid var(--navy);box-shadow:0 0 0 2px #fff inset}

.motto{position:absolute;left:12px;top:598px;width:168px;font-family:"Oswald",sans-serif;font-weight:500;font-size:17px;line-height:22px;color:var(--white)}
.motto__mark{display:block;color:var(--gold);font-size:28px;line-height:18px;margin-left:38px}
.motto__look{color:var(--gold);margin-left:52px}
.motto__yellow{color:var(--gold)}

/* ---------- back ---------- */
.back-inner{position:absolute;left:19px;top:19px;right:19px;bottom:5px;background:linear-gradient(160deg,#fff 0%,#f3f4f6 45%,#fff 70%)}
.pillar{position:absolute;left:0;right:0;height:36px;display:flex;align-items:center}
.pillar__label{flex:0 0 80px;font-family:"Oswald",sans-serif;font-weight:500;font-size:15px;color:var(--navy);text-align:right;white-space:nowrap}
.pillar__letter{flex:0 0 24px;text-align:center;font-family:"Oswald",sans-serif;font-weight:700;font-size:46px;line-height:36px;color:var(--gold);-webkit-text-stroke:1.5px var(--navy)}
.pillar__rest{font-family:"Oswald",sans-serif;font-weight:500;font-size:15px;color:var(--navy);border-bottom:2px solid var(--navy);white-space:nowrap}
.pillar__text{flex:1;margin-left:14px;margin-right:10px;font-size:7px;line-height:9.6px;color:var(--navy)}

.partner{position:absolute;font-family:"Montserrat",sans-serif;font-weight:600;color:var(--blue);font-size:11px;line-height:13px;text-align:center;display:flex;flex-direction:column;align-items:center;gap:5px}
.partner__shape{display:block;width:40px;height:40px;border-radius:50%;background:#d8e4f0}
.partner__shape--square{border-radius:4px}
.footer-brand{position:absolute;left:104px;top:672px;width:60px;text-align:center;font-family:"Montserrat",sans-serif;font-weight:700;font-size:7px;color:var(--blue);line-height:1.15}
.footer-brand .brand__dot{width:30px;height:30px}
.footer-note{position:absolute;left:176px;top:716px;font-family:"Montserrat",sans-serif;font-weight:600;font-size:10.5px;color:var(--navy);letter-spacing:.3px}
</style>
</head>
<body>

<section class="page page--front" aria-label="Front page">
  <div class="front-inner">
    <div class="scenery" role="img" aria-label="Photo of the island coastline with blue ocean and forested headland"></div>

    <div class="brand"><span class="brand__dot"></span>TQR Habitat Stewards</div>
    <h1 class="headline">Make a difference</h1>
    <div class="headline__year">IN 2019</div>

    <p class="intro intro--top">The best way to experience the true beauty of Tarqueen Island is to see it for yourself; join our TQR Habitat Stewards program in 2019 and be involved in a world class, award winning holistic conservation effort – protecting paradise.</p>
    <blockquote class="quote">“Tarqueen Island is so extraordinary it is almost unbelievable”.<cite>SIR EDMUND HALLOWAY</cite></blockquote>
    <p class="intro intro--over">The best way to experience the true beauty of Tarqueen Island is to see it for yourself; join our TQR Habitat Stewards program in 2019 and be involved in a world class, award winning holistic conservation effort – protecting paradise.</p>

    <article class="event">
      <div class="event__box" style="left:95px;top:229px;width:374px;min-height:64px;padding-top:10px">
        <h2 class="event__title">Birds of Tarqueen Island – May 2019</h2>
        <p class="event__text">Showcasing Tarqueen Island’s incredible bird species. Experience the amazing phenomena of ‘calling’ wild seabirds down from the sky as you assist in research into the life of rare seabirds.</p>
      </div>
      <div class="event__photo" role="img" aria-label="Photo of a seabird chick in its nest" style="left:7px;top:217px;width:88px;height:88px;background:radial-gradient(circle,#8a8b88,#5b5647 70%)"></div>
    </article>

    <article class="event">
      <div class="event__box" style="left:123px;top:345px;width:368px;min-height:64px;padding-top:9px">
        <h2 class="event__title">Tarqueen Island’s Marine Environment – June 2019</h2>
        <p class="event__text">Our seabirds are being impacted by ocean plastic debris. Help survey Tarqueen Island’s diverse intertidal ecosystems and provide valuable data to help understand the issue and support solutions.</p>
      </div>
      <div class="event__photo" role="img" aria-label="Photo of a snorkeller surveying the reef underwater" style="left:35px;top:329px;width:88px;height:88px;background:radial-gradient(circle,#3c8fc4,#1a4f82 75%)"></div>
    </article>

    <article class="event">
      <div class="event__box" style="left:167px;top:448px;width:335px;min-height:64px">
        <h2 class="event__title">Invasive Species – July 2019</h2>
        <p class="event__text">Invasive weeds are identified as one of the most serious threats to Tarqueen Island’s biodiversity and world heritage values. Hike to remote and settlement locations and assist in weed removal with our experts, whilst learning about our world class Weed Eradication Program</p>
      </div>
      <div class="event__photo" role="img" aria-label="Photo of a green mountain ridge with a hiker" style="left:83px;top:435px;width:88px;height:88px;background:radial-gradient(circle,#8fa7a0,#3f5c3a 70%)"></div>
    </article>

    <article class="event">
      <div class="event__box" style="left:213px;top:553px;width:301px;padding-top:4px;padding-bottom:4px">
        <h2 class="event__title">Amazing Invertebrates – August 2019</h2>
        <p class="event__text" style="font-size:6.8px;line-height:9px">Rodents are voracious predators of invertebrates. The loss of invertebrates is particularly significant because invertebrates play an important role in maintaining natural ecological functions. This month we will celebrate the discovery and revival of the rare Phasmid and the wider context of invertebrate conservation on Tarqueen Island and across the globe.</p>
      </div>
      <div class="event__photo" role="img" aria-label="Photo of volunteers gathered in the forest" style="left:127px;top:537px;width:88px;height:88px;background:radial-gradient(circle,#b9b4a2,#4d5b3b 70%)"></div>
    </article>

    <article class="event">
      <div class="event__box" style="left:272px;top:652px;width:244px;padding:4px 6px 4px 24px;background:rgba(255,253,238,.97)">
        <h2 class="event__title" style="font-size:8.8px;line-height:11px">Protecting Paradise – September 2019</h2>
        <p class="event__text" style="font-size:6.6px;line-height:8.6px">September will showcase the very best of our island conservation. Tarqueen Island has a long history of sustainability and conservation programs ensuring the Island’s unique biodiversity is safeguarded. Recently winning the prestigious national gold coral award as well as the sustainability award for government, adding to 2 Green Orbit awards and a RESA award in 2018.</p>
      </div>
      <div class="event__photo" role="img" aria-label="Photo of a child exploring a rock pool" style="left:183px;top:645px;width:92px;height:92px;background:radial-gradient(circle,#d9c6b3,#6f87a0 75%)"></div>
    </article>

    <p class="motto"><span class="motto__mark">“</span><span class="motto__look">LOOK</span><br>deeper into nature<br><span class="motto__yellow">YOU WILL UNDERSTAND</span><br>EVERYTHING BETTER”</p>
  </div>
</section>

<section class="page page--back" aria-label="Back page">
  <div class="back-inner">
    <div class="pillar" style="top:32px">
      <span class="pillar__label">PROTECTING</span><span class="pillar__letter">P</span><span class="pillar__rest">ARADISE</span>
      <p class="pillar__text">Tarqueen Island is considered to be an outstanding example of an island ecosystem developed from submarine volcanic activity. One of the last settled islands in the world, Tarqueen Island’s almost untouched environment needs to be protected.</p>
    </div>
    <div class="pillar" style="top:82px">
      <span class="pillar__label">WO</span><span class="pillar__letter">R</span><span class="pillar__rest">LD HERITAGE</span>
      <p class="pillar__text">In 1982, The Tarqueen Island Group was listed as a Global Heritage Council World Heritage property, in recognition of the global significance of the island’s beauty and biodiversity.</p>
    </div>
    <div class="pillar" style="top:118px">
      <span class="pillar__label">CONSERVATI</span><span class="pillar__letter">O</span><span class="pillar__rest">N VOLUNTEERS</span>
      <p class="pillar__text">Connect with nature through conservation and contribute to data collection used to aid research on environmental issues</p>
    </div>
    <div class="pillar" style="top:152px">
      <span class="pillar__label">ADVEN</span><span class="pillar__letter">T</span><span class="pillar__rest">URE</span>
      <p class="pillar__text">The perfect place for true adventure, unexplored environments, undiscovered species, all level hiking, unique activities and amazing views.</p>
    </div>
    <div class="pillar" style="top:186px">
      <span class="pillar__label">CITIZ</span><span class="pillar__letter">E</span><span class="pillar__rest">N SCIENCE</span>
      <p class="pillar__text">Citizen science is, reconnecting people with wildlife and the environment helping science and conservation and sparking imaginations and passions in the process.</p>
    </div>
    <div class="pillar" style="top:224px">
      <span class="pillar__label">WORLD</span><span class="pillar__letter">C</span><span class="pillar__rest">LASS</span>
      <p class="pillar__text">Tarqueen Island’s renowned pristine natural environment is maintained through world-class conservation efforts that began more than 100 years ago and continue today.</p>
    </div>
    <div class="pillar" style="top:266px">
      <span class="pillar__label">RELAXA</span><span class="pillar__letter">T</span><span class="pillar__rest">ION</span>
      <p class="pillar__text">Breathtaking scenery, pristine environment, no mobile reception. The perfect place to take some time out and relax.</p>
    </div>

    <div class="partner" style="left:22px;top:400px;width:120px"><span class="partner__shape"></span>Tarqueen Island Museum</div>
    <div class="partner" style="left:170px;top:392px;width:130px"><span class="partner__shape"></span>Tarqueen Island Board</div>
    <div class="partner" style="left:345px;top:392px;width:150px"><span class="partner__shape partner__shape--square"></span>Eastland Primary Industries</div>

    <div class="partner" style="left:14px;top:516px;width:140px;font-size:12px;line-height:15px">Tarqueen Island just paradise</div>
    <div class="partner" style="left:190px;top:500px;width:110px"><span class="partner__shape partner__shape--square"></span>Southmark Zoos</div>
    <div class="partner" style="left:345px;top:500px;width:150px"><span class="partner__shape partner__shape--square"></span>Eastland Office of Environment &amp; Heritage</div>

    <div class="partner" style="left:14px;top:584px;width:120px"><span class="partner__shape partner__shape--square"></span>Continental Museum</div>
    <div class="partner" style="left:180px;top:584px;width:130px"><span class="partner__shape"></span>Meridian Coast University</div>
    <div class="partner" style="left:355px;top:580px;width:130px"><span class="partner__shape"></span>Harbourline Zoo</div>

    <div class="footer-brand"><span class="brand__dot"></span>TQR Habitat Stewards</div>
    <p class="footer-note">for more details: www.tarqueenisland.info</p>
  </div>
</section>

</body>
</html>
```